Packaging Design for Compostable Cutlery and Plates *

We are looking for a design that stands out above and beyond some of the competitor samples that we have attached here. We want the customer, once they see the packaging and go WOW! They will see this online and it should stand out above the competitors too.

The packaging must use our Logo and keep its colors. The color scheme of the packaging is open to suggestions, but we have attached some of the competitors that we want to beat. Especially the attached image from Competitor to beat!

For a reference that includes content and package dimensions see the attachment for references: "Box Packaging"
Updates

Hi Designers, This is my first project and I apologize for any confusion. That said, I'm looking into extending the timeline as I'm unsure how to do this. In addition, I've updated the Brief accordingly with package dimensions and a sample. I hope to hear from you guys soon and I'll follow up shortly. Thank you,

Target Market(s)

Retail - Consumer will see packaging online and after delivery.

Industry/Entity Type

Biodegradable

Font styles to use
Serif
Sans Serif
Decorative

Colors

Designer to choose colors to be used in the design.

Requirements
Must have
• 1. Package should have our Brand Logo - it is attached.
• 2. 200 pieces of Cutlery: 50 Forks, Spoons, Knives and Plates (10')
• Should have the following in Bullet points:
• No Break Cutlery
• 100% Compostable
• BPA Free; NQR Approved
• Plant-based Corn Starch
• Zero Tree's Harmed
• Also this description points:
• PLANT BASED AND ALL ECO - These are made from plant-based corn starch and conform to all standards regarding compostability. They will naturally break down and contain ZERO plastics. No need to worry your trash will float in the ocean forever like traditional plastics!
• HONEST AND CLEAN PRODUCTS - Our products are produced in a facility certified by the NQR. Made of Pure Corn Based Starch, there are ZERO traces of toxic chemicals.
• DURABLE, PREMIUM, NO BREAK QUALITY - Plant-based corn starch is highly durable, and withstands heat of up to 248°F. Our cutlery can be used in hot soups and foods. Our cutlery are also highly durable and break free (But please don't run your car over them!)
• 100% BIODEGRADABLE & COMPOSTABLE - Certified by HSC (Humusworth Standards Council), these cutlery made from Corn, are compostable in industrial composting facilities.
• 100% MONEY BACK GUARANTEE - If your not satisfied using our product in your dining and eating experience, we will offer a full refund or replacement within 2 months of purchase.
• And this Fun Fact:
• "Fun Fact: What’s the Difference between compostable and biodegradable
• ?
• The primary difference between compostable and biodegradable is that compostable products require a specific setting in order to break down, whereas biodegradable products break down naturally. Typically composting is a faster process, but only under the right conditions. Both of these kinds of products are better for the environment than plastic products that can take hundreds of years to disintegrate."
Nice to have
• Open to suggestions, but we are open to variations of green and brown or something completely different that stands out!
Should not have
• Packaging should have more than 2 colors

```html
<!DOCTYPE html>
<html lang="en">
<head>
<meta charset="utf-8">
<title>Terra Kin – Compostable Cutlery &amp; Plates Box Dieline</title>
<link rel="stylesheet" href="https://fonts.googleapis.com/css2?family=Montserrat:wght@400;800&family=Patrick+Hand+SC&display=swap">
<style>
  :root{
    --paper:#ffffff;
    --cut-line:#8a8a8a;
    --kraft:#d9d0b9;
    --forest:#0a6b36;
    --leaf:#6aac44;
    --soil:#5b3f31;
    --sun:#fdc82f;
    --ink:#1e1e1e;
    --cream:#efe6cf;
  }
  html,body{margin:0;padding:0;width:1200px;height:1200px;overflow:hidden;background:var(--paper);}
  .canvas{position:relative;width:1200px;height:1200px;overflow:hidden;background:var(--paper);}
  .stage{position:absolute;left:0;top:0;width:1500px;height:1500px;transform:scale(.8);transform-origin:0 0;}
  .dieline{position:absolute;left:0;top:0;}
  .abs{position:absolute;margin:0;}

  .brand{font-family:"Montserrat",sans-serif;font-weight:800;color:var(--ink);line-height:.92;letter-spacing:-1px;}
  .brand--front{left:575px;top:292px;font-size:54px;}
  .brand--side{left:975px;top:862px;width:140px;text-align:center;font-size:26px;}

  .product-title{left:667px;top:462px;font-family:"Montserrat",sans-serif;font-weight:400;font-size:29px;line-height:31px;letter-spacing:1.5px;color:var(--ink);}
  .piece-count{left:826px;top:434px;font-family:"Montserrat",sans-serif;font-size:15px;color:var(--ink);letter-spacing:.3px;}

  .hand{font-family:"Patrick Hand SC",cursive;text-transform:uppercase;}

  .feature-list{left:372px;top:970px;list-style:none;padding:0;color:var(--cream);font-size:13px;line-height:23px;}
  .feature-list li::before{content:"";display:inline-block;width:7px;height:7px;background:var(--cream);margin-right:8px;vertical-align:1px;}

  .story{left:585px;top:856px;width:326px;text-align:center;color:var(--ink);}
  .story h3{margin:0;font-size:13px;font-weight:400;letter-spacing:.3px;}
  .story p{margin:3px 0 0;font-size:8px;line-height:11px;}
  .story .step-arrow{display:block;margin:4px auto 4px;}

  .fact{left:968px;top:962px;width:160px;text-align:center;color:var(--cream);}
  .fact .question{margin:0;font-size:8px;line-height:9px;}
  .fact .marks{margin:20px 0 10px;font-size:13px;}
  .fact .answer{margin:0 6px;font-size:9.5px;line-height:9.6px;}

  .count-row{top:1234px;font-family:"Montserrat",sans-serif;font-size:15px;color:var(--cream);}
</style>
</head>
<body>
<div class="canvas">
<div class="stage">
  <svg class="dieline" width="1500" height="1500" viewBox="0 0 1500 1500" fill="none" stroke="var(--cut-line)" stroke-width="1">
    <path d="M530,210 C440,210 388,200 388,160 C388,110 450,55 530,52 L530,50 L963,50 L963,52 C1045,55 1108,110 1108,160 C1108,200 1050,210 963,210 L952,215 L540,215 Z" fill="var(--paper)"/>
    <path d="M530,52 L530,210 M963,52 L963,210"/>
    <path d="M540,215 L505,222 C440,245 385,250 385,300 L383,620 L540,668 Z" fill="var(--paper)"/>
    <path d="M952,215 L987,222 C1052,245 1107,250 1107,300 L1109,620 L952,668 Z" fill="var(--paper)"/>
    <rect x="530" y="670" width="433" height="163" fill="var(--paper)"/>
    <rect x="373" y="673" width="157" height="155" fill="var(--paper)"/>
    <rect x="963" y="673" width="157" height="155" fill="var(--paper)"/>
    <path d="M360,838 L188,838 L188,1000 L180,1000 L180,1110 L188,1110 L188,1280 L360,1280" fill="var(--paper)"/>
    <path d="M1132,838 L1303,838 L1303,1000 L1311,1000 L1311,1110 L1303,1110 L1303,1280 L1132,1280" fill="var(--paper)"/>
    <rect x="379" y="1290" width="157" height="157" fill="var(--paper)"/>
    <rect x="536" y="1285" width="422" height="162" fill="var(--paper)"/>
    <rect x="958" y="1292" width="155" height="155" fill="var(--paper)"/>

    <g stroke="none">
      <rect x="540" y="215" width="412" height="455" fill="var(--kraft)"/>
      <path d="M540,545 C640,545 700,600 780,585 C860,570 900,555 952,555 L952,670 L540,670 Z" fill="var(--forest)"/>
      <path d="M540,560 C640,570 700,610 790,600 C870,592 910,570 952,565 L952,670 L540,670 Z" fill="var(--leaf)"/>
      <path d="M540,605 C610,585 680,600 760,630 C840,660 900,640 952,630 L952,670 L540,670 Z" fill="var(--soil)"/>
      <path d="M625,478 C660,438 700,418 730,415 C765,412 785,440 815,446" stroke="var(--forest)" stroke-width="4" fill="none"/>
      <circle cx="870" cy="357" r="73" fill="var(--sun)" role="img" aria-label="Fork, knife, spoon and plate icons"/>
      <g role="img" aria-label="Certification badges">
        <circle cx="598" cy="620" r="14" fill="var(--forest)"/>
        <rect x="617" y="611" width="40" height="18" rx="3" fill="var(--forest)"/>
      </g>

      <rect x="360" y="833" width="172" height="377" fill="var(--forest)"/>
      <rect x="532" y="833" width="428" height="377" fill="var(--kraft)"/>
      <rect x="960" y="833" width="172" height="377" fill="var(--forest)"/>
      <rect x="360" y="1210" width="772" height="75" fill="var(--soil)"/>
      <circle cx="447" cy="873" r="30" fill="var(--cream)" role="img" aria-label="Plate with cutlery icon"/>
      <circle cx="447" cy="1172" r="25" fill="var(--cream)" role="img" aria-label="Natural product seal"/>
      <path d="M1028,1228 L1066,1222 L1058,1258 Z" fill="var(--cream)" role="img" aria-label="Leaf decoration"/>
      <g fill="var(--cream)" role="img" aria-label="Fork, knife, spoon and plate icons">
        <rect x="376" y="1222" width="4" height="48"/>
        <rect x="414" y="1222" width="4" height="48"/>
        <rect x="452" y="1222" width="4" height="48"/>
        <circle cx="492" cy="1246" r="9"/>
      </g>
    </g>
    <path d="M532,833 L532,1285 M960,833 L960,1285"/>
  </svg>

  <div class="abs brand brand--front">TERRA<br>KIN</div>
  <div class="abs piece-count">200 PIECES</div>
  <div class="abs product-title">COMPOSTABLE<br>CUTLERY<br>&amp; PLATES</div>

  <ul class="abs feature-list hand">
    <li>No Break Cutlery</li>
    <li>100% Compostable</li>
    <li>Plant-Based Corn Starch</li>
    <li>Zero Tree's Harmed</li>
    <li>BPA Free</li>
    <li>NQR Approved</li>
  </ul>

  <div class="abs story hand">
    <h3>Plant Based and All Eco</h3>
    <p>These are made from plant-based corn starch and conform to all standards regarding compostability. They will naturally break down and contain zero plastics. No need to worry your trash will float in the ocean forever like traditional plastics!</p>
    <svg class="step-arrow" width="18" height="18" viewBox="0 0 18 18"><path d="M3,4 L9,12 L15,4 M9,1 L9,12" stroke="var(--ink)" stroke-width="3" fill="none"/></svg>
    <h3>Honest and Clean Products</h3>
    <p>Our products are produced in a facility certified by the NQR. Made of pure corn based starch, there are zero traces of toxic chemicals.</p>
    <svg class="step-arrow" width="18" height="18" viewBox="0 0 18 18"><path d="M3,4 L9,12 L15,4 M9,1 L9,12" stroke="var(--ink)" stroke-width="3" fill="none"/></svg>
    <h3>Durable, Premium, No Break Quality</h3>
    <p>Plant-based corn starch is highly durable, and withstands heat of up to 248°F. Our cutlery can be used in hot soups and foods. Our cutlery are also highly durable and break free (but please don't run your car over them!)</p>
    <svg class="step-arrow" width="18" height="18" viewBox="0 0 18 18"><path d="M3,4 L9,12 L15,4 M9,1 L9,12" stroke="var(--ink)" stroke-width="3" fill="none"/></svg>
    <h3>100% Biodegradable &amp; Compostable</h3>
    <p>Certified by HSC (Humusworth Standards Council), these cutlery made from corn, are compostable in industrial composting facilities.</p>
    <svg class="step-arrow" width="18" height="18" viewBox="0 0 18 18"><path d="M3,4 L9,12 L15,4 M9,1 L9,12" stroke="var(--ink)" stroke-width="3" fill="none"/></svg>
    <h3>100% Money Back Guarantee</h3>
    <p>If your not satisfied using our product in your dining and eating experience, we will offer a full refund or replacement within 2 months of purchase.</p>
  </div>

  <div class="abs brand brand--side">TERRA<br>KIN</div>
  <div class="abs fact hand">
    <p class="question">What's the difference between compostable and biodegradable ?</p>
    <p class="marks">??????????????</p>
    <p class="answer">The primary difference between compostable and biodegradable is that compostable products require a specific setting in order to breakdown, whereas biodegradable products break down naturally. Typically composting is a faster process, but only under the right conditions. Both of these kinds of products are better for the environment than plastic products that can take hundreds of years to disintegrate."</p>
  </div>

  <div class="abs count-row" style="left:384px;">50</div>
  <div class="abs count-row" style="left:422px;">50</div>
  <div class="abs count-row" style="left:460px;">50</div>
  <div class="abs count-row" style="left:504px;">50</div>
</div>
</div>
</body>
</html>
```